Maple Lantern Business Card

Colors can be blue, grey and white as you see in the attached logo. Needs to have a spot for name, title, phone, email, address, and website. There also needs to be a spot for an agent's picture.

Contact Information for Business Card

See project description.

Colors

Designer to choose colors to be used in the design.

```html
<!DOCTYPE html>
<html lang="en">
<head>
<meta charset="utf-8">
<title>Maple Lantern Business Card</title>
<link rel="stylesheet" href="https://fonts.googleapis.com/css2?family=Roboto:wght@400;500;700&display=swap">
<style>
  :root {
    --backdrop: #2b2b2d;
    --card-white: #ffffff;
    --brand-blue: #2775b6;
    --brand-grey: #515153;
    --text-grey: #4a4a4c;
    --rule-grey: #8a8a8c;
    --photo-light: #dfe6ee;
    --photo-dark: #b7c4d3;
  }
  * { box-sizing: border-box; margin: 0; padding: 0; }
  html, body { width: 1200px; height: 1108px; overflow: hidden; }
  body {
    background: var(--backdrop);
    font-family: "Roboto", sans-serif;
    position: relative;
  }
  .card {
    position: absolute;
    top: 204px;
    width: 420px;
    height: 700px;
    border-radius: 30px;
    overflow: hidden;
  }
  .card--front { left: 150px; background: var(--card-white); }
  .card--back { left: 630px; background: var(--brand-grey); }

  .brand {
    position: absolute;
    left: 0; right: 0;
    text-align: center;
  }
  .brand__name {
    font-weight: 700;
    font-size: 38px;
    letter-spacing: 1px;
    text-transform: uppercase;
    line-height: 1;
  }
  .brand__tag {
    margin: 10px auto 0;
    width: 270px;
    font-weight: 500;
    font-size: 17px;
    letter-spacing: 5px;
    text-transform: uppercase;
    display: flex;
    align-items: center;
    gap: 10px;
  }
  .brand__tag::before, .brand__tag::after {
    content: "";
    flex: 1;
    height: 2px;
    background: currentColor;
  }
  .card--front .brand { top: 84px; color: var(--brand-blue); }
  .card--front .brand__tag { color: var(--brand-grey); }
  .brand__mark {
    display: block;
    width: 22px; height: 22px;
    margin: 0 auto 14px;
    background: var(--brand-blue);
  }

  .agent-photo {
    position: absolute;
    top: 226px;
    left: 50%;
    width: 112px; height: 112px;
    margin-left: -56px;
    border-radius: 50%;
    border: 3px solid var(--brand-blue);
    background: linear-gradient(160deg, var(--photo-light), var(--photo-dark));
  }

  .agent {
    position: absolute;
    top: 352px; left: 0; right: 0;
    text-align: center;
  }
  .agent__name { color: var(--brand-blue); font-weight: 700; font-size: 30px; line-height: 1.2; }
  .agent__title { color: var(--text-grey); font-size: 21px; margin-top: 2px; }

  .icon-row {
    position: absolute;
    top: 432px; left: 60px; right: 60px;
    display: flex; align-items: center; gap: 8px;
  }
  .icon-row::before, .icon-row::after {
    content: ""; flex: 1; height: 1.5px; background: var(--rule-grey);
  }
  .icon-row svg { width: 26px; height: 26px; }

  .contact {
    position: absolute;
    top: 474px; left: 0; right: 0;
    text-align: center;
    color: var(--text-grey);
    font-size: 21px;
    line-height: 1.35;
  }
  .contact__web-accent { color: var(--brand-blue); }
  .divider {
    position: absolute;
    top: 572px; left: 70px; right: 70px;
    height: 1.5px; background: var(--rule-grey);
  }
  .address {
    position: absolute;
    top: 590px; left: 0; right: 0;
    text-align: center;
    color: var(--text-grey);
    font-size: 21px;
    line-height: 1.35;
  }

  .back-shape { position: absolute; inset: 0; }
  .card--back .brand { top: 540px; color: var(--card-white); }
  .card--back .brand__name { font-size: 40px; }
</style>
</head>
<body>
  <section class="card card--front" aria-label="Card front">
    <div class="brand">
      <span class="brand__mark"></span>
      <div class="brand__name">Maple Lantern</div>
      <div class="brand__tag">Real Estate</div>
    </div>

    <div class="agent-photo" role="img" aria-label="Agent portrait photo"></div>

    <div class="agent">
      <div class="agent__name">Daniel Harper</div>
      <div class="agent__title">Manager</div>
    </div>

    <div class="icon-row">
      <svg viewBox="0 0 26 26" aria-label="Phone"><circle cx="13" cy="13" r="13" fill="#2775b6"/><path d="M8 10c0-1.5 2-2 2.5-1l1 2c.3.6-.6 1.3-.6 1.3.6 1.3 1.6 2.3 2.9 2.9 0 0 .7-.9 1.3-.6l2 1c1 .5.5 2.5-1 2.5C11 18 8 15 8 10z" fill="#fff"/></svg>
      <svg viewBox="0 0 26 26" aria-label="Email"><circle cx="13" cy="13" r="13" fill="#2775b6"/><rect x="6.5" y="8.5" width="13" height="9" fill="none" stroke="#fff" stroke-width="1.6"/><path d="M6.5 8.5l6.5 5 6.5-5" fill="none" stroke="#fff" stroke-width="1.6"/></svg>
      <svg viewBox="0 0 26 26" aria-label="Website"><circle cx="13" cy="13" r="13" fill="#2775b6"/><circle cx="13" cy="13" r="6.5" fill="none" stroke="#fff" stroke-width="1.5"/><ellipse cx="13" cy="13" rx="2.8" ry="6.5" fill="none" stroke="#fff" stroke-width="1.3"/><path d="M6.5 13h13" stroke="#fff" stroke-width="1.3"/></svg>
    </div>

    <div class="contact">
      <div>555-014-2100</div>
      <div>youremail@mailbox.com</div>
      <div>www.<span class="contact__web-accent">yourwebsite</span>.com</div>
    </div>
    <div class="divider"></div>
    <div class="address">
      <div>Your address, city</div>
      <div>state, ZIP 0000</div>
    </div>
  </section>

  <section class="card card--back" aria-label="Card back">
    <svg class="back-shape" viewBox="0 0 420 700" preserveAspectRatio="none">
      <polygon points="0,355 290,292 420,520 420,700 0,700" fill="#ffffff"/>
      <polygon points="0,378 285,318 420,548 420,700 0,700" fill="#2775b6"/>
    </svg>
    <div class="brand">
      <div class="brand__name">Maple Lantern</div>
      <div class="brand__tag">Real Estate</div>
    </div>
  </section>
</body>
</html>
```